Lumora Learning Web Design Project

Who We are:
Lumora Learning is education information portal/ magazine, providing information about the Chinese and International education markets. Our aim is to help school principals improve there curriculum, and parents in understanding this curriculum.

Project Brief:
The site will include education news updates, educational services, curriculum developments and overseas study. We hope the site represents the cross cultural bridge between the west and east. The site will cover both the Sciences and Arts.

Note:
The logo design competition is also underway so we only need the website design

What We want:
This competition is for Design only no coding!
Design a home page based on Template 1,2 or 3. I only need to select one.
The design of an article page.

Optional
Design a Microsoft Windows metro style splash page.

Sites We like:
http://www.kavelin.com.cn/kavelinlingo/default.aspx
http://www.brixtalacademia.co.uk/
http://qrpv.norvatestudio.net/

Template Explanations:
Template 1-
The main information has a dynamic sliding category view that when clicked displays the relevant info.
In addition to the main upper menu it also has a left hand sliding menu that pops out on click or gesture

Template 2-
Has limited number of Articles most of the menus are drop downs from the top menu

Template 3-
No Top menu

Target Market(s)

Teachers, principals and parents

Industry/Entity Type

Education

Requirements
Should not have
• kindergarten preschool feel

```html
<!DOCTYPE html>
<html lang="en">
<head>
<meta charset="utf-8">
<title>Lumora Learning — Splash</title>
<link rel="stylesheet" href="https://fonts.googleapis.com/css2?family=Source+Sans+3:wght@400;600&display=swap">
<style>
  :root {
    --bg: #ffffff;
    --rule: #dcdcdc;
    --brand-red: #d9262b;
    --brand-blue: #1d5a92;
    --tile-crimson: #a1171f;
    --tile-cyan: #03a6cc;
    --tile-navy: #0b287a;
    --tile-midnight: #022456;
    --tile-coral: #ff583b;
    --tile-clay: #c4714a;
    --tile-green: #12cc00;
    --text-light: #ffffff;
    --footer-text: #8a8a8a;
    --social-1: #3b5a9a;
    --social-2: #6ec4e6;
    --social-3: #f28a00;
    --social-4: #8ccbea;
    --social-5: #0f75bb;
  }
  * { margin: 0; padding: 0; box-sizing: border-box; }
  html, body {
    width: 1200px; height: 1000px; overflow: hidden;
    background: var(--bg);
  }
  .splash {
    position: relative; width: 1200px; height: 1000px;
    font-family: "Source Sans 3", "Myriad Pro", sans-serif;
  }
  .brand {
    position: absolute; left: 0; top: 140px; width: 1200px;
    display: flex; justify-content: center; align-items: center; gap: 12px;
  }
  .brand-dot {
    width: 22px; height: 22px; border-radius: 50%;
    background: var(--brand-blue);
  }
  .brand-name {
    color: var(--brand-red); font-weight: 600; font-size: 28px;
    letter-spacing: 0.5px; text-transform: uppercase;
  }
  .rule {
    position: absolute; height: 3px; background: var(--rule);
  }
  .rule--top { left: 38px; top: 221px; width: 1120px; }
  .rule--bottom { left: 40px; top: 908px; width: 1120px; }

  .tile {
    position: absolute; display: block; color: var(--text-light);
    text-decoration: none; text-transform: uppercase; font-weight: 400;
    letter-spacing: -0.5px;
  }
  .tile--sm { font-size: 27px; line-height: 30px; padding: 12px 14px; }
  .tile--md { font-size: 54px; line-height: 50px; padding: 28px 24px; }
  .tile--lg { font-size: 84px; line-height: 80px; padding: 14px 18px; letter-spacing: -1.5px; }

  .tile--one   { left: 40px;  top: 245px; width: 670px; height: 305px; background: var(--tile-crimson); }
  .tile--two   { left: 715px; top: 245px; width: 220px; height: 150px; background: var(--tile-cyan); }
  .tile--three { left: 940px; top: 245px; width: 220px; height: 150px; background: var(--tile-navy); }
  .tile--four  { left: 715px; top: 400px; width: 445px; height: 370px; background: var(--tile-midnight); }
  .tile--five  { left: 40px;  top: 555px; width: 220px; height: 150px; background: var(--tile-coral); }
  .tile--six   { left: 265px; top: 555px; width: 445px; height: 305px; background: var(--tile-clay); }
  .tile--seven { left: 40px;  top: 710px; width: 220px; height: 150px; background: var(--tile-cyan); }
  .tile--six.tile--md { padding-top: 26px; }

  .enter {
    position: absolute; left: 715px; top: 775px; width: 445px; height: 85px;
    background: var(--tile-green); color: var(--text-light);
    display: flex; align-items: center; justify-content: center;
    font-size: 48px; text-decoration: none; letter-spacing: -1px;
    text-transform: uppercase;
  }

  .footer-note {
    position: absolute; left: 40px; top: 940px;
    font-family: Arial, Helvetica, sans-serif; font-size: 13px;
    color: var(--footer-text);
  }
  .social {
    position: absolute; top: 928px; left: 958px; height: 32px;
    list-style: none;
  }
  .social li {
    position: absolute; top: 0; width: 32px; height: 32px; border-radius: 2px;
  }
  .social .s1 { left: 0;   background: var(--social-1); }
  .social .s2 { left: 42px;  background: var(--social-2); }
  .social .s3 { left: 84px;  background: var(--social-3); }
  .social .s4 { left: 130px; background: var(--social-4); }
  .social .s5 { left: 172px; background: var(--social-5); }
</style>
</head>
<body>
<main class="splash">
  <header class="brand">
    <span class="brand-dot" aria-hidden="true"></span>
    <span class="brand-name">Lumora Learning</span>
  </header>
  <div class="rule rule--top"></div>

  <nav class="tiles" aria-label="Categories">
    <a class="tile tile--lg tile--one" href="#">Category<br>One</a>
    <a class="tile tile--sm tile--two" href="#">Category<br>Two</a>
    <a class="tile tile--sm tile--three" href="#">Category<br>Three</a>
    <a class="tile tile--md tile--four" href="#">Category<br>Four</a>
    <a class="tile tile--sm tile--five" href="#">Category<br>Five</a>
    <a class="tile tile--md tile--six" href="#">Category<br>Six</a>
    <a class="tile tile--sm tile--seven" href="#">Category<br>Seven</a>
    <a class="enter" href="#">Enter Site &gt;&gt;&gt;</a>
  </nav>

  <div class="rule rule--bottom"></div>
  <footer>
    <p class="footer-note">© 2013 Lumora Learning</p>
    <ul class="social" aria-label="Social links">
      <li class="s1" aria-label="Social network link"></li>
      <li class="s2" aria-label="Social network link"></li>
      <li class="s3" aria-label="News feed link"></li>
      <li class="s4" aria-label="Video channel link"></li>
      <li class="s5" aria-label="Professional network link"></li>
    </ul>
  </footer>
</main>
</body>
</html>
```